Design for a 4 screens iOS and Android app - "VelidMetra"

The app allows you to track your car gasoline refill ...
We need a design for the 4 screens of the app:
a) 1 form with 3 fields.
b) 1 simple list view
c) 1 summary view
d) 1 text page
2 "alerts" items are also to be designed.
No specific guidelines, nor logo or whatever.
It will be a free app distributed on iOS and Androïd.
We just want to make it looking nice & very usable for end users.
Target Market(s)
B2C app
Industry/Entity Type
Android

```html
<!DOCTYPE html>
<html lang="en">
<head>
<meta charset="utf-8">
<title>VelidMetra – app screens</title>
<link href="https://fonts.googleapis.com/css2?family=Ubuntu:wght@400;500;700&display=swap" rel="stylesheet">
<style>
:root{
  --green:#3cb81e;
  --green-dark:#2f9a17;
  --green-light:#7fd45c;
  --bg:#e4e4e4;
  --panel:#f2f2f2;
  --white:#ffffff;
  --field:#e3e3e3;
  --field-line:#cfcfcf;
  --ink:#1d1d1d;
  --muted:#8a8a8a;
  --tabbar:#2a2a2a;
  --tab-off:#7a7a7a;
}
*{box-sizing:border-box;margin:0;padding:0}
html,body{width:1200px;height:1200px;overflow:hidden}
body{
  background:radial-gradient(circle at 50% 50%,#f4f4f4 0%,var(--bg) 70%);
  font-family:'Ubuntu',sans-serif;color:var(--ink);position:relative;
}
.screen{position:absolute;width:214px;height:378px;overflow:hidden;background:var(--panel);box-shadow:0 2px 10px rgba(0,0,0,.12)}
.col-1{left:118px}.col-2{left:482px}.col-3{left:845px}
.row-1{top:128px}.row-2{top:703px}

/* splash */
.splash{background:radial-gradient(circle at 50% 45%,#86d968 0%,#4fb530 55%,#3a9a22 100%);color:var(--white)}
.status-bar{height:14px;display:flex;justify-content:space-between;align-items:center;padding:0 5px;font-size:7px}
.brand{position:absolute;left:0;right:0;top:205px;text-align:center}
.brand-row{display:flex;align-items:center;justify-content:center;gap:6px}
.brand-mark{width:12px;height:12px;background:var(--white)}
.brand-name{font-size:19px;font-weight:700;letter-spacing:.5px}
.brand-tag{font-size:4.6px;letter-spacing:1.3px;margin-top:3px}

/* app bar */
.app-bar{height:34px;background:var(--green);display:flex;justify-content:space-between;align-items:center;padding:0 14px 0 13px}
.app-bar svg{display:block}

/* form */
.form{padding:0 18px}
.field-label{font-size:13px;margin:20px 0 7px 2px}
.field-label:first-child{margin-top:19px}
.input{height:31px;background:var(--field);border:1px solid var(--field-line);font-size:11.5px;padding:0 7px;display:flex;align-items:center}
.select{justify-content:space-between;padding-right:0}
.select .chev{width:33px;height:100%;border-left:1px solid var(--field-line);display:flex;align-items:center;justify-content:center}
.save{margin-top:26px;height:30px;background:var(--green);color:var(--white);font-size:12.5px;display:flex;align-items:center;justify-content:center}
.dim{position:absolute;left:0;right:0;top:0;bottom:0;background:rgba(0,0,0,.22)}
.alert{position:absolute;left:18px;top:146px;width:181px;height:63px;background:var(--white);text-align:center}
.alert-title{height:38px;line-height:40px;font-size:12.5px;border-bottom:1px solid #dcdcdc}
.alert-ok{line-height:24px;font-size:11px}

/* tabs */
.tabs{height:26px;background:var(--tabbar);display:flex}
.tab{flex:1;display:flex;align-items:center;padding-left:17px;font-size:12.5px;color:var(--tab-off);border-left:1px solid #3a3a3a}
.tab:first-child{border-left:0;color:var(--white)}
.tab:last-child{justify-content:flex-end;padding-right:9px}

/* summary */
.month-head{height:36px;display:flex;justify-content:space-between;align-items:center;padding:0 25px 0 13px;font-size:12.5px}
.month-head .rate{color:var(--green)}
.stats{height:35px;display:flex}
.stat{flex:1;padding:6px 0 0 11px;border-left:1px solid #dedede}
.stat:first-child{border-left:0}
.stat-label{font-size:5px;color:var(--muted);letter-spacing:.2px}
.stat-value{font-size:11.5px;margin-top:4px}
.tone-a .month-head{background:var(--panel)}.tone-a .stats{background:var(--white)}
.tone-b .month-head{background:var(--white)}.tone-b .stats{background:var(--panel)}

/* refill list */
.refill-date{height:33px;display:flex;align-items:center;padding-left:11px;font-size:10px;font-weight:500}
.refill-data{height:24px;display:flex;font-size:7.5px;color:#444}
.refill-data span{flex:1;display:flex;align-items:center;justify-content:center;border-left:1px solid #dedede}
.refill-data span:first-child{border-left:0;justify-content:flex-start;padding-left:15px}
.refill.tone-a .refill-date{background:var(--panel)}.refill.tone-a .refill-data{background:var(--white)}
.refill.tone-b .refill-date{background:var(--white)}.refill.tone-b .refill-data{background:var(--panel)}
.refill .refill-date{border-top:1px solid #e4e4e4}

/* about */
.about{background:var(--panel);text-align:center}
.close{position:absolute;right:16px;top:22px;font-size:16px;line-height:1;color:#222}
.about .brand{top:102px;color:var(--ink)}
.about .brand-mark{background:var(--green)}
.about .brand-name{font-size:17px}
.about .brand-tag{font-size:4.3px;color:#555}
.about-text{position:absolute;left:19px;right:15px;top:144px;font-size:6.9px;line-height:8.8px;text-align:left}
.about-url{position:absolute;left:0;right:0;top:338px;font-size:6.3px;letter-spacing:1.3px}
</style>
</head>
<body>

<!-- splash -->
<section class="screen splash col-1 row-1">
  <div class="status-bar"><span>●●●○○ NOVA</span><span>4:21 PM</span><span>100% ▮</span></div>
  <div class="brand">
    <div class="brand-row"><span class="brand-mark"></span><span class="brand-name">VELIDMETRA</span></div>
    <div class="brand-tag">TRACK YOUR CAR GASOLINE REFILL</div>
  </div>
</section>

<!-- refill form -->
<section class="screen col-2 row-1">
  <header class="app-bar">
    <svg width="12" height="12" viewBox="0 0 12 12"><path d="M6 0v12M0 6h12" stroke="#fff" stroke-width="1.8"/></svg>
    <svg width="13" height="12" viewBox="0 0 13 12"><path d="M0 1.5h13M0 6h13M0 10.5h13" stroke="#fff" stroke-width="1.8"/></svg>
    <svg width="14" height="12" viewBox="0 0 14 12"><path d="M1 0v11h13" stroke="#fff" stroke-width="1.6" fill="none"/><path d="M3 10V6l3-3 3 3 3-2v6z" fill="#fff"/></svg>
  </header>
  <div class="form">
    <div class="field-label">Gasoline</div>
    <div class="input">120 ltr</div>
    <div class="field-label">Volume</div>
    <div class="input select"><span>Liters</span><span class="chev"><svg width="10" height="6" viewBox="0 0 10 6"><path d="M1 1l4 4 4-4" stroke="#333" stroke-width="1.3" fill="none"/></svg></span></div>
    <div class="field-label">Cost</div>
    <div class="input select"><span>USD</span><span class="chev"><svg width="10" height="6" viewBox="0 0 10 6"><path d="M1 1l4 4 4-4" stroke="#333" stroke-width="1.3" fill="none"/></svg></span></div>
    <div class="save">Save</div>
  </div>
</section>

<!-- saved alert -->
<section class="screen col-3 row-1">
  <header class="app-bar">
    <svg width="12" height="12" viewBox="0 0 12 12"><path d="M6 0v12M0 6h12" stroke="#fff" stroke-width="1.8"/></svg>
    <svg width="13" height="12" viewBox="0 0 13 12"><path d="M0 1.5h13M0 6h13M0 10.5h13" stroke="#fff" stroke-width="1.8"/></svg>
    <svg width="14" height="12" viewBox="0 0 14 12"><path d="M1 0v11h13" stroke="#fff" stroke-width="1.6" fill="none"/><path d="M3 10V6l3-3 3 3 3-2v6z" fill="#fff"/></svg>
  </header>
  <div class="form">
    <div class="field-label">Gasoline</div>
    <div class="input">120 ltr</div>
    <div class="field-label">Volume</div>
    <div class="input select"><span>Liters</span><span class="chev"></span></div>
    <div class="field-label">Cost</div>
    <div class="input select"><span>USD</span><span class="chev"><svg width="10" height="6" viewBox="0 0 10 6"><path d="M1 1l4 4 4-4" stroke="#333" stroke-width="1.3" fill="none"/></svg></span></div>
    <div class="save">Save</div>
  </div>
  <div class="dim"></div>
  <div class="alert">
    <div class="alert-title">Data Saved</div>
    <div class="alert-ok">OK</div>
  </div>
</section>

<!-- monthly summary -->
<section class="screen col-1 row-2">
  <header class="app-bar">
    <svg width="12" height="12" viewBox="0 0 12 12"><path d="M6 0v12M0 6h12" stroke="#fff" stroke-width="1.8"/></svg>
    <svg width="13" height="12" viewBox="0 0 13 12"><path d="M0 1.5h13M0 6h13M0 10.5h13" stroke="#fff" stroke-width="1.8"/></svg>
    <svg width="14" height="12" viewBox="0 0 14 12"><path d="M1 0v11h13" stroke="#fff" stroke-width="1.6" fill="none"/><path d="M3 10V6l3-3 3 3 3-2v6z" fill="#fff"/></svg>
  </header>
  <nav class="tabs"><span class="tab">2016</span><span class="tab">2015</span><span class="tab">2014</span></nav>
  <div class="month tone-a">
    <div class="month-head"><span>January 2016</span><span class="rate">6.1</span></div>
    <div class="stats"><div class="stat"><div class="stat-label">TOTAL COST</div><div class="stat-value">570.54 €</div></div><div class="stat"><div class="stat-label">MILAGE</div><div class="stat-value">7500 KM</div></div><div class="stat"><div class="stat-label">FUEL TANKS</div><div class="stat-value">11</div></div></div>
  </div>
  <div class="month tone-b">
    <div class="month-head"><span>February 2016</span><span class="rate">6.1</span></div>
    <div class="stats"><div class="stat"><div class="stat-label">TOTAL COST</div><div class="stat-value">570.54 €</div></div><div class="stat"><div class="stat-label">MILAGE</div><div class="stat-value">7500 KM</div></div><div class="stat"><div class="stat-label">FUEL TANKS</div><div class="stat-value">11</div></div></div>
  </div>
  <div class="month tone-a">
    <div class="month-head"><span>March 2016</span><span class="rate">6.1</span></div>
    <div class="stats"><div class="stat"><div class="stat-label">TOTAL COST</div><div class="stat-value">570.54 €</div></div><div class="stat"><div class="stat-label">MILAGE</div><div class="stat-value">7500 KM</div></div><div class="stat"><div class="stat-label">FUEL TANKS</div><div class="stat-value">11</div></div></div>
  </div>
  <div class="month tone-b">
    <div class="month-head"><span>April 2016</span><span class="rate">6.1</span></div>
    <div class="stats"><div class="stat"><div class="stat-label">TOTAL COST</div><div class="stat-value">570.54 €</div></div><div class="stat"><div class="stat-label">MILAGE</div><div class="stat-value">7500 KM</div></div><div class="stat"><div class="stat-label">FUEL TANKS</div><div class="stat-value">11</div></div></div>
  </div>
  <div class="month tone-a">
    <div class="month-head"><span>March 2016</span><span class="rate">6.1</span></div>
  </div>
</section>

<!-- refill list -->
<section class="screen col-2 row-2">
  <header class="app-bar">
    <svg width="12" height="12" viewBox="0 0 12 12"><path d="M6 0v12M0 6h12" stroke="#fff" stroke-width="1.8"/></svg>
    <svg width="13" height="12" viewBox="0 0 13 12"><path d="M0 1.5h13M0 6h13M0 10.5h13" stroke="#fff" stroke-width="1.8"/></svg>
    <svg width="14" height="12" viewBox="0 0 14 12"><path d="M1 0v11h13" stroke="#fff" stroke-width="1.6" fill="none"/><path d="M3 10V6l3-3 3 3 3-2v6z" fill="#fff"/></svg>
  </header>
  <nav class="tabs"><span class="tab">JAN</span><span class="tab">FEB</span><span class="tab">MAR</span></nav>
  <div class="refill tone-a"><div class="refill-date">15 Jan. 2016 14:24</div><div class="refill-data"><span>127500&nbsp; km</span><span>49.88</span><span>47.25€</span></div></div>
  <div class="refill tone-b"><div class="refill-date">15 Jan. 2016 14:24</div><div class="refill-data"><span>127500&nbsp; km</span><span>49.88</span><span>47.25€</span></div></div>
  <div class="refill tone-a"><div class="refill-date">15 Jan. 2016 14:24</div><div class="refill-data"><span>127500&nbsp; km</span><span>49.88</span><span>47.25€</span></div></div>
  <div class="refill tone-b"><div class="refill-date">15 Jan. 2016 14:24</div><div class="refill-data"><span>127500&nbsp; km</span><span>49.88</span><span>47.25€</span></div></div>
  <div class="refill tone-a"><div class="refill-date">15 Jan. 2016 14:24</div><div class="refill-data"><span>127500&nbsp; km</span><span>49.88</span><span>47.25€</span></div></div>
  <div class="refill tone-b"><div class="refill-date">15 Jan. 2016 14:24</div></div>
</section>

<!-- about page -->
<section class="screen about col-3 row-2">
  <div class="close">✕</div>
  <div class="brand">
    <div class="brand-row"><span class="brand-mark"></span><span class="brand-name">VELIDMETRA</span></div>
    <div class="brand-tag">TRACK YOUR CAR GASOLINE REFILL</div>
  </div>
  <p class="about-text">VelidMetra keeps a simple log of every refill you make. Enter the amount of fuel, choose the volume unit and the currency, then save the entry in one tap. Each month the app adds up your total cost, the distance driven and the number of tanks filled, so you can see at a glance how much your car really consumes. Browse past years and months from the tabs at the top, open any refill to check its date, mileage, price per unit and total. Your data stays on your phone and is never shared. Drive smart, spend less and always know what your next trip will cost you.</p>
  <div class="about-url">WWW.FUELNOTE.EXAMPLE</div>
</section>

</body>
</html>
```